Need Business Card for our Real Estate Business with Sales Executive's Picture

PANTONE 484 C ( RED)

PANTONE 2766 C ( BLUE

Industry/Entity Type

Real Estate

Contact Information for Business Card

Name, Mobile, email, & picture of Person
Agency Phone, address, Web address

Requirements
Must have
• Our Logo Colours, Agent Picture,

```html
<!DOCTYPE html>
<html lang="en">
<head>
<meta charset="utf-8">
<title>Meridian Real Estate – Business Card</title>
<link rel="stylesheet" href="https://fonts.googleapis.com/css2?family=Cinzel:wght@500&family=Tinos&display=swap">
<style>
  :root {
    --navy: #1e2156;
    --crimson: #8a1c24;
    --paper: #ffffff;
    --paper-shade: #eeeeef;
    --backdrop: #d4d4d4;
    --ink: #1a1a1a;
  }
  * { margin: 0; padding: 0; box-sizing: border-box; }
  html, body { width: 900px; height: 1200px; overflow: hidden; }
  body { background: var(--backdrop); position: relative; font-family: "Tinos", serif; }

  .card { position: absolute; left: 97px; width: 700px; height: 410px; box-shadow: 0 3px 6px rgba(0,0,0,.35); overflow: hidden; }
  .card--front { top: 157px; background: var(--navy); }
  .card--back { top: 632px; background: linear-gradient(180deg, var(--paper) 0%, var(--paper-shade) 60%, var(--paper) 100%); }

  .brand { position: absolute; text-align: center; font-family: "Cinzel", serif; font-weight: 500; }
  .brand__name { display: block; letter-spacing: 3px; line-height: 1; }
  .brand__square { display: inline-block; width: 10px; height: 10px; background: var(--crimson); margin-bottom: 12px; }
  .card--front .brand { left: 0; right: 0; top: 150px; color: var(--paper); }
  .card--front .brand__name { font-size: 46px; }
  .card--back .brand { left: 395px; width: 270px; top: 130px; color: var(--navy); }
  .card--back .brand__name { font-size: 46px; }

  .portrait { position: absolute; left: 38px; top: 10px; width: 142px; height: 250px;
    background: linear-gradient(180deg, #e9e4e1 0%, #3a4f9a 40%, #26357c 100%); border-radius: 40px 40px 0 0; }

  .name-band { position: absolute; left: 0; top: 260px; width: 700px; height: 56px; background: var(--navy); }
  .name-band__notch { position: absolute; left: 499px; top: 29px; }
  .person { position: absolute; left: 52px; top: 7px; color: var(--paper); font-family: "Cinzel", serif; font-weight: 500; }
  .person__name { font-size: 21px; letter-spacing: 1px; line-height: 24px; }
  .person__role { font-size: 16px; letter-spacing: 1px; line-height: 22px; }

  .contacts { position: absolute; top: 328px; font-size: 15px; color: var(--ink); line-height: 22px; }
  .contacts--personal { left: 52px; }
  .contacts--address { left: 274px; top: 326px; }
  .contacts--agency { left: 516px; }
  .contact { display: flex; align-items: center; gap: 7px; }
  .contact svg { flex: none; }

  .base-band { position: absolute; left: 0; bottom: 0; width: 700px; height: 15px; background: var(--navy); }
</style>
</head>
<body>
  <section class="card card--front" aria-label="Card front">
    <div class="brand">
      <span class="brand__square"></span>
      <span class="brand__name">MERIDIAN</span>
    </div>
  </section>

  <section class="card card--back" aria-label="Card back">
    <div class="portrait" role="img" aria-label="Portrait photo of the managing director in a blue suit"></div>

    <div class="brand">
      <span class="brand__square"></span>
      <span class="brand__name">MERIDIAN</span>
    </div>

    <div class="name-band">
      <svg class="name-band__notch" width="62" height="27" viewBox="0 0 62 27"><polygon points="0,27 31,0 62,27" fill="#fff"/></svg>
      <div class="person">
        <div class="person__name">DANIEL ARCHER</div>
        <div class="person__role">MANAGING DIRECTOR</div>
      </div>
    </div>

    <div class="contacts contacts--personal">
      <div class="contact">
        <svg width="17" height="17" viewBox="0 0 17 17"><circle cx="8.5" cy="8.5" r="8.5" fill="var(--crimson)"/><rect x="5.5" y="3.5" width="6" height="10" rx="1" fill="none" stroke="#fff" stroke-width="1.3"/></svg>
        <span>335-0471-5928</span>
      </div>
      <div class="contact">
        <svg width="17" height="17" viewBox="0 0 17 17"><circle cx="8.5" cy="8.5" r="8.5" fill="var(--crimson)"/><rect x="4" y="5.5" width="9" height="6" fill="none" stroke="#fff" stroke-width="1.2"/><polyline points="4,5.5 8.5,9 13,5.5" fill="none" stroke="#fff" stroke-width="1.2"/></svg>
        <span>danielarcher@meridian.au</span>
      </div>
    </div>

    <div class="contacts contacts--address">
      <div>118/42 Harbour Lane</div>
      <div>Kelso Bay, NSW 2590, Australia</div>
    </div>

    <div class="contacts contacts--agency">
      <div class="contact">
        <svg width="17" height="17" viewBox="0 0 17 17"><circle cx="8.5" cy="8.5" r="8.5" fill="var(--navy)"/><path d="M5 4.5l2 0 1 2.5-1.3 1a6 6 0 0 0 2.8 2.8l1-1.3 2.5 1 0 2c-4.5 .5-8.5-3.5-8-8z" fill="#fff"/></svg>
        <span>402-618-3374</span>
      </div>
      <div class="contact">
        <svg width="17" height="17" viewBox="0 0 17 17"><circle cx="8.5" cy="8.5" r="8.5" fill="var(--navy)"/><circle cx="8.5" cy="8.5" r="4.5" fill="none" stroke="#fff" stroke-width="1"/><ellipse cx="8.5" cy="8.5" rx="2" ry="4.5" fill="none" stroke="#fff" stroke-width="1"/><line x1="4" y1="8.5" x2="13" y2="8.5" stroke="#fff" stroke-width="1"/></svg>
        <span>www.meridian.au</span>
      </div>
    </div>

    <div class="base-band"></div>
  </section>
</body>
</html>
```